GLNW Website and Inner page template

Home page website design with inner page design for template. Details below as well as in txt document included
Project Description: New website for a current client ( GLNW ) .. current website is located at https://www.glnw.example/Home.aspx
I need a home page design with an inner page design that will be used as a template ( 2 pages )
Logo is attached
Important notes:
Every page has to include the mission and vision. See below
"Our mission: to protect the public by promoting excellence in chiropractic regulation through service to our member boards
Our vision: The GLNW is the premier international resource for information and consolidated services for ensuring the safe, ethical practice of chiropractic"
Social media icons on the head of every page
facebook
twitter
linkedin
instagram
youtube
Every page needs to include the phone number on the header and footer
Main navigation links ( they are going to be different from current website ). Since most of these links are going to have sub-menus, please show the rollover affect. I have included the sub-menu options for "Get Started". The sub-menu should not be in a "list style" because the sub-menu links are categorized in some cases. A good example on their current website is to roll over the "Services" link in the main navigation
"Get Started" Sub-menu options ( categories and links )
- Chiropractic Regulators
- Annual Meeting
- District Meetings
- Licensing Board Information
- Library
- Administrators ( DRMOT )
- Legal Advisors ( DRMOT )
- Other Chiropractic Organizations
- Chiropractic Patients
- How to check a license
- Look up a license
- Request a Disciplinary Report
- Consumer Information
- Registered Chiropractors & Chiropractic Assistants
- Continuing Education Courses
- Chiropractic Assistant
- Certification
- View your continuing Ed Credits
Full list if primary navigation links:
Home
Contact
Company Info
Chiropractic Boards
Resources
Services
Get Started
Home Page Specifics:
"Hero Banner" or large "Slider" image with text at top of page below main navigation
4 primary points of interest to highlight
- VEX-TOR ( verified examiner exchange trust oversight registry )
- LOOM ( Sponsors of Vetted Ongoing Learning )
- TMRH ( Trained Manipulative Rehab Helpers )
- Wayfinder ( Openly Viewable Practitioner Verification )
Large "Member Access" area with the following links inside it
- Register for meetings
- Pay an Invoice
- VEX-TOR
- LOOM
- TMRH
- Report to VEX-TOR
- DRMOT Login
Large "Get Started" section with 3 categories that have links
- Chiropractic Regulators
- Annual Meeting
- District Meetings
- Library
- Chiropractic Patients
- How to Check a license
- Look up a license
- Consumer Information
- Coninuing Education Courses
- Chiropractic Assistant
- Certification
- View Your Continuing Ed Credits
Inner page specifics:
The inner page should look similar to the home page at the header and footer areas then have a large area for content. No large images or anything like that needed..
IMPORTANT... ONLY USE GRAPHICS/IMAGES from pixvault imagery. ( https://www.pixvaultimagery.example/ ) This is important because we have an account with them so you can use the watermarked images then when I build the website I can easily purchase the licensing rights for those images. You dont' need an account to do searches, locate images and use the water marked image in the design.
Target Market(s)
Chiropractic Licensing
Number of Pages Required
2 page
Requirements
Must have
- Please see attached document
Nice to have
Should not have

```html
<!DOCTYPE html>
<html lang="en">
<head>
<meta charset="utf-8">
<title>GLNW – Home</title>
<link href="https://fonts.googleapis.com/css2?family=Crimson+Text:wght@400;600;700&family=Poppins:wght@400;500;600&display=swap" rel="stylesheet">
<style>
:root{
  --navy:#2b5a92;
  --navy-dark:#234c7e;
  --bright:#1a8cf0;
  --ink:#1b1b1b;
  --grey:#6b6b6b;
  --link:#2b5a92;
  --white:#fff;
}
*{margin:0;padding:0;box-sizing:border-box}
html,body{width:1200px;height:3011px;overflow:hidden;background:var(--white)}
body{position:relative;font-family:"Poppins",sans-serif;color:var(--ink)}
.abs{position:absolute}
.serif{font-family:"Crimson Text",serif}

/* top bar */
.topbar{left:75px;top:0;width:1049px;height:33px;background:var(--navy);border-radius:0 0 28px 28px;color:#fff;font-size:13px}
.topbar .phone{left:70px;top:8px;font-weight:600;font-size:15px}
.topbar .mail{left:348px;top:9px}
.topbar svg{position:absolute}
.socials{display:flex;gap:10px}
.socials span{width:13px;height:13px;border-radius:50%;background:#fff;display:block}
.topbar .socials{position:absolute;right:60px;top:10px}

/* header */
.brand{left:61px;top:47px;display:flex;align-items:center;gap:10px}
.brand .mark{width:48px;height:52px;background:var(--navy)}
.brand .name{font-family:"Crimson Text",serif;font-size:21px;line-height:19px;color:var(--navy);width:180px}
.nav{left:440px;top:64px;display:flex;gap:24px;font-size:13px;color:#555}
.nav .active{color:var(--navy)}
.btn{background:var(--bright);color:#fff;font-weight:600;text-align:center;border-radius:6px}
.btn-head{left:997px;top:52px;width:142px;height:36px;line-height:36px;font-size:15px}

/* hero */
.hero{left:0;top:112px;width:1200px;height:690px;background:linear-gradient(100deg,#c9d6e4 0%,#e9eef3 40%,#f2f2f0 70%,#e6e9ea 100%)}
.hero-title{right:61px;top:312px;text-align:right;font-family:"Crimson Text",serif;font-weight:700;font-size:52px;line-height:53px;color:#111}
.hero-title .blue{color:var(--navy)}
.btn-hero{left:998px;top:493px;width:142px;height:36px;line-height:36px;font-size:15px}

/* sections */
.section-title{width:1200px;left:0;text-align:center;font-family:"Crimson Text",serif;font-size:29px}
.section-title .blue{color:var(--navy)}
.underline{height:2px;background:var(--navy)}

.quick{top:952px;width:260px;text-align:center}
.quick .badge{width:150px;height:74px;margin:0 auto;background:linear-gradient(135deg,#e6ebf2,#f8f9fb)}
.quick h3{font-family:"Crimson Text",serif;font-weight:700;font-size:18px;margin-top:18px}
.quick p{font-size:13px;color:var(--grey);line-height:19px;margin-top:6px}

/* member */
.member-title{color:#fff}
.access{width:240px;text-align:center;color:#fff}
.access .disc{width:112px;height:112px;margin:0 auto;border-radius:50%;background:#fff;clip-path:inset(0 0 14% 0);position:relative}
.access .disc svg{position:absolute;left:31px;top:22px}
.access .label{font-family:"Crimson Text",serif;font-weight:600;font-size:19px;margin-top:0px}

/* what we do */
.card{top:1880px;width:301px;height:556px;background:#fff;border-radius:150px 150px 0 0/120px 120px 0 0;box-shadow:0 0 16px rgba(0,0,0,.09);text-align:center}
.card .photo{position:absolute;left:15px;top:17px;width:271px;height:271px;border-radius:50%}
.card .notch{position:absolute;left:100px;top:200px;width:100px;height:100px;border-radius:50%;background:#fff}
.card .notch svg{position:absolute;left:26px;top:12px}
.card h3{position:absolute;top:270px;width:100%;font-family:"Crimson Text",serif;font-weight:600;font-size:20px}
.card ul{position:absolute;top:315px;width:100%;list-style:none;font-size:12.5px;line-height:30px}
.card a{color:var(--link)}
.card .btn-card{position:absolute;left:94px;top:535px;width:112px;height:28px;line-height:28px;border-radius:14px;background:var(--navy);color:#fff;font-size:13px;font-weight:600}

/* footer */
.footer-text{color:#fff}
.f-brand{left:61px;top:2657px}
.f-brand .mark{background:#fff}
.f-brand .name{color:#fff}
.mission{left:61px;top:2744px;width:250px;font-size:13px;line-height:19px;color:#fff}
.fcol{top:2660px;color:#fff}
.fcol h4{font-family:"Crimson Text",serif;font-weight:400;font-size:20px}
.fcol ul{list-style:none;margin-top:14px;font-size:13px;line-height:30px}
.contact-item{color:#fff;font-size:13px}
.copy{left:61px;top:2979px;color:#fff;font-size:12px}
.f-socials{right:61px;top:2982px}
</style>
</head>
<body>

<!-- top bar -->
<div class="abs topbar">
  <svg style="left:68px;top:8px" width="18" height="18" viewBox="0 0 24 24"><path d="M6 3l3 4-2 2c1 3 4 6 7 7l2-2 4 3-2 4C10 21 3 14 3 5z" fill="#fff"/></svg>
  <span class="abs phone" style="left:114px">555.204.7180</span>
  <svg style="left:312px;top:9px" width="20" height="14" viewBox="0 0 20 14"><rect x="1" y="1" width="18" height="12" fill="none" stroke="#fff" stroke-width="1.5"/><path d="M1 1l9 7 9-7" fill="none" stroke="#fff" stroke-width="1.5"/></svg>
  <span class="abs mail">info@guildoflicensingnetworks.example</span>
  <div class="socials" aria-label="Social media"><span></span><span></span><span></span><span></span><span></span></div>
</div>

<!-- header -->
<div class="abs brand"><div class="mark"></div><div class="name">Guild of Licensing Networks Worldwide</div></div>
<nav class="abs nav"><span class="active">Home</span><span>Company Info</span><span>Chiropractic Boards</span><span>Resources</span><span>Services</span><span>Contact</span></nav>
<div class="abs btn btn-head">GET STARTED</div>

<!-- hero -->
<div class="abs hero" role="img" aria-label="Chiropractor in blue scrubs adjusting a patient's shoulder in a bright clinic room"></div>
<svg class="abs" style="left:0;top:700px" width="1200" height="110" viewBox="0 700 1200 110">
  <path d="M0,724 Q600,860 1200,724 L1200,810 L0,810Z" fill="#fff"/>
  <path d="M0,724 Q600,860 1200,724" fill="none" stroke="var(--bright)" stroke-width="5"/>
</svg>
<h1 class="abs hero-title">The Public by Promoting<br>Excellence <span class="blue">in Chiropractic<br>Regulation</span></h1>
<div class="abs btn btn-hero">GET STARTED</div>

<!-- quicklinks -->
<h2 class="abs section-title" style="top:880px">GLNW Services <span class="blue">- Quicklinks</span></h2>
<div class="abs underline" style="left:563px;top:918px;width:74px"></div>
<div class="abs quick" style="left:56px"><div class="badge"></div><h3>VEX-TOR</h3><p>Verified Examiner Exchange Trust<br>Oversight Registry</p></div>
<div class="abs quick" style="left:331px"><div class="badge"></div><h3>LOOM</h3><p>Sponsors of Vetted Ongoing<br>Learning</p></div>
<div class="abs quick" style="left:607px"><div class="badge"></div><h3>TMRH</h3><p>Trained Manipulative Rehab<br>Helpers</p></div>
<div class="abs quick" style="left:883px"><div class="badge"></div><h3>Wayfinder</h3><p>Openly Viewable Practitioner<br>Verification</p></div>

<!-- member access -->
<svg class="abs" style="left:0;top:1180px" width="1200" height="560" viewBox="0 1180 1200 560" role="img" aria-label="Blue-tinted photo of a practitioner treating a patient">
  <defs><linearGradient id="memberBg" x1="0" y1="0" x2="1" y2="1"><stop offset="0" stop-color="#3d679b"/><stop offset=".5" stop-color="#4a73a4"/><stop offset="1" stop-color="#2e5d94"/></linearGradient></defs>
  <path d="M0,1256 Q600,1116 1200,1256 L1200,1740 L0,1740Z" fill="url(#memberBg)"/>
  <path d="M0,1256 Q600,1116 1200,1256" fill="none" stroke="var(--bright)" stroke-width="5"/>
</svg>
<h2 class="abs section-title member-title" style="top:1258px">Member Access</h2>
<div class="abs underline" style="left:565px;top:1296px;width:70px;background:#fff"></div>

<div class="abs access" style="left:66px;top:1340px"><div class="disc"><svg width="50" height="50" viewBox="0 0 50 50" fill="none" stroke="#2b5a92" stroke-width="2"><rect x="4" y="4" width="42" height="20"/><path d="M4 12h42M22 30v16M16 36h12"/></svg></div><div class="label">Register for meetings</div></div>
<div class="abs access" style="left:341px;top:1340px"><div class="disc"><svg width="50" height="50" viewBox="0 0 50 50" fill="none" stroke="#2b5a92" stroke-width="2"><rect x="6" y="6" width="38" height="30"/><path d="M14 14h22M14 20h22M14 26h14M18 44h14"/></svg></div><div class="label">Pay an Invoice</div></div>
<div class="abs access" style="left:617px;top:1340px"><div class="disc"><svg width="50" height="50" viewBox="0 0 50 50" fill="none" stroke="#2b5a92" stroke-width="2"><path d="M25 4v42M18 10h14M18 20h14M18 30h14M18 40h14"/></svg></div><div class="label">VEX-TOR</div></div>
<div class="abs access" style="left:893px;top:1340px"><div class="disc"><svg width="50" height="50" viewBox="0 0 50 50" fill="none" stroke="#2b5a92" stroke-width="2"><circle cx="18" cy="14" r="7"/><path d="M6 44V30h24v14M30 8h14v14H30"/></svg></div><div class="label">LOOM</div></div>

<div class="abs access" style="left:201px;top:1520px"><div class="disc"><svg width="50" height="50" viewBox="0 0 50 50" fill="none" stroke="#2b5a92" stroke-width="2"><path d="M10 4h22l8 8v26H10z"/><path d="M16 16h18M16 22h18M16 28h10"/><circle cx="25" cy="40" r="5"/></svg></div><div class="label">TMRH</div></div>
<div class="abs access" style="left:477px;top:1520px"><div class="disc"><svg width="50" height="50" viewBox="0 0 50 50" fill="none" stroke="#2b5a92" stroke-width="2"><rect x="12" y="4" width="26" height="38" rx="3"/><path d="M18 26v-6M24 26v-10M30 26v-4"/></svg></div><div class="label">Report to VEX-TOR</div></div>
<div class="abs access" style="left:752px;top:1520px"><div class="disc"><svg width="50" height="50" viewBox="0 0 50 50" fill="none" stroke="#2b5a92" stroke-width="2"><rect x="4" y="6" width="42" height="34"/><path d="M4 14h42"/><circle cx="25" cy="24" r="4"/><path d="M16 34h18"/></svg></div><div class="label">DRMOT Login</div></div>

<!-- what we do -->
<h2 class="abs section-title" style="top:1810px">What We Do</h2>

<div class="abs card" style="left:119px">
  <div class="photo" role="img" aria-label="Doctor showing a spine model to a smiling patient" style="background:linear-gradient(135deg,#d8d2cc,#f1ece8 50%,#c6cbd2)"></div>
  <div class="notch"><svg width="48" height="48" viewBox="0 0 48 48" fill="none" stroke="#2b5a92" stroke-width="2"><rect x="2" y="6" width="40" height="28"/><path d="M10 14h24M10 20h16"/><circle cx="36" cy="36" r="6"/></svg></div>
  <h3>Chiropractic Regulators</h3>
  <ul><li><a>Annual Meeting</a></li><li><a>District Meetings</a></li><li><a>Licensing Board Information</a></li><li><a>Library</a></li><li><a>Administrators ( DRMOT )</a></li><li><a>Legal Advisors ( DRMOT )</a></li><li><a>Other Chiropractic Organizations</a></li></ul>
  <div class="btn-card">GET STARTED</div>
</div>

<div class="abs card" style="left:450px">
  <div class="photo" role="img" aria-label="Hand pointing at a spine vertebrae model" style="background:linear-gradient(135deg,#e9e4df,#cdb9a8 50%,#9d8a7c)"></div>
  <div class="notch"><svg width="48" height="48" viewBox="0 0 48 48" fill="none" stroke="#2b5a92" stroke-width="2"><circle cx="24" cy="8" r="5"/><path d="M14 30l10-16 10 16M4 34h40M10 34v10M38 34v10"/></svg></div>
  <h3>Chiropractic Patients</h3>
  <ul><li><a>How to Check a license</a></li><li><a>Look up a license</a></li><li><a>Request a Disciplinary Report</a></li><li><a>Consumer Information</a></li></ul>
  <div class="btn-card">GET STARTED</div>
</div>

<div class="abs card" style="left:779px">
  <div class="photo" role="img" aria-label="Chiropractor examining a patient's back in an office" style="background:linear-gradient(135deg,#cfd5da,#eeecea 50%,#d9cfc8)"></div>
  <div class="notch"><svg width="48" height="48" viewBox="0 0 48 48" fill="none" stroke="#2b5a92" stroke-width="2"><rect x="6" y="6" width="28" height="38"/><path d="M12 16h16M12 24h16M12 32h10M30 40l12-14"/></svg></div>
  <h3>Registered Chiropractors</h3>
  <ul><li><a>Coninuing Education Courses</a></li><li><a>Chiropractic Assistant</a></li><li><a>Certification</a></li><li><a>View Your Continuing Ed Credits</a></li></ul>
  <div class="btn-card">GET STARTED</div>
</div>

<!-- footer -->
<svg class="abs" style="left:0;top:2530px" width="1200" height="481" viewBox="0 2530 1200 481">
  <path d="M0,2605 Q600,2465 1200,2605 L1200,3011 L0,3011Z" fill="var(--navy)"/>
  <path d="M0,2605 Q600,2465 1200,2605" fill="none" stroke="var(--bright)" stroke-width="5"/>
</svg>
<div class="abs brand f-brand"><div class="mark"></div><div class="name">Guild of Licensing Networks Worldwide</div></div>
<p class="abs mission">to protect the public by promoting excellence in chiropractic regulation through service to our member boards</p>

<div class="abs fcol" style="left:338px"><h4>Site Map</h4><ul><li>- Home</li><li>- Contact</li><li>- Company Info</li><li>- Chiropractic Boards</li><li>- Resources</li><li>- Services</li><li>- Get Started</li></ul></div>
<div class="abs fcol" style="left:613px"><h4>Company</h4><ul><li>- Contact Us</li><li>- Query VEX-TOR</li><li>- Manage LOOM Courses</li><li>- Pay Invoice</li><li>- For Our Board</li><li>- Login</li></ul></div>
<div class="abs fcol" style="left:889px"><h4>Contact Us</h4></div>

<svg class="abs" style="left:889px;top:2710px" width="18" height="22" viewBox="0 0 18 22" fill="none" stroke="#fff" stroke-width="1.6"><path d="M9 21s7-7 7-12A7 7 0 0 0 2 9c0 5 7 12 7 12z"/><circle cx="9" cy="9" r="2.5"/></svg>
<span class="abs contact-item" style="left:920px;top:2712px">2870 Larkspur Avenue, Suite 204</span>
<svg class="abs" style="left:889px;top:2768px" width="20" height="20" viewBox="0 0 24 24"><path d="M6 3l3 4-2 2c1 3 4 6 7 7l2-2 4 3-2 4C10 21 3 14 3 5z" fill="none" stroke="#fff" stroke-width="1.6"/></svg>
<span class="abs contact-item" style="left:920px;top:2771px">555.204.7180</span>
<svg class="abs" style="left:889px;top:2820px" width="20" height="20" viewBox="0 0 20 20" fill="none" stroke="#fff" stroke-width="1.6"><rect x="5" y="1" width="10" height="6"/><rect x="1" y="7" width="18" height="8"/><rect x="5" y="12" width="10" height="7"/></svg>
<span class="abs contact-item" style="left:920px;top:2823px">555.204.7181</span>
<svg class="abs" style="left:889px;top:2877px" width="20" height="14" viewBox="0 0 20 14"><rect x="1" y="1" width="18" height="12" fill="none" stroke="#fff" stroke-width="1.5"/><path d="M1 1l9 7 9-7" fill="none" stroke="#fff" stroke-width="1.5"/></svg>
<span class="abs contact-item" style="left:920px;top:2877px">info@glnw.example</span>

<p class="abs copy">Copyright 2021 by GLNW | Privacy Statement | Terms Of Use</p>
<div class="abs socials f-socials" aria-label="Social media"><span></span><span></span><span></span><span></span><span></span></div>

</body>
</html>
```